Kestrel Building Works Business Card and more!

We need a business card design for Kestrel Building Works Ltd, a respected building company that specialises in high quality designer homes.

We're after a sleek, clean, modern business card that incorporates our new logo (see attached) and colours, with black being the background.

We are Certified Trade Craftsmen and need to include their logo (see attached) on our cards, balancing but not taking over our logo.

Details to be included:

Warren Pike
Director

Phone: 0219462513
Email: kestrelbuild.nz@mailbox-example.nz
Website: www.kestrelbuildingworks.co.nz

Additional Information

A start up website is also under construction and needing attention and letterheads are needed!

We look forward to your designs!

Target Market(s)

30+ people who are interested in building new or renovating current homes

Industry/Entity Type

Construction

Contact Information for Business Card

Warren Pike
Director

Phone: 0219462513
Facebook: www.socialpage-example.com/kestrelbuild.nz

Font styles to use
Serif

Colors

Designer to choose colors to be used in the design.

Requirements
Must have
• Our new logo
• Our colours
• ctc logo

```html
<!DOCTYPE html>
<html lang="en">
<head>
<meta charset="utf-8">
<title>Kestrel Building Works – Business Card</title>
<link href="https://fonts.googleapis.com/css2?family=Montserrat:wght@600;700&family=Open+Sans:wght@400&display=swap" rel="stylesheet">
<style>
  :root {
    --backdrop: #3a3a36;
    --card: #141414;
    --card-edge: #1f1f1f;
    --gold: #c9965f;
    --white: #f4f1ec;
    --muted: #d8d4cc;
  }
  * { box-sizing: border-box; margin: 0; padding: 0; }
  html, body {
    width: 1200px; height: 824px; overflow: hidden;
    background: var(--backdrop);
  }
  .stage {
    width: 1200px; height: 824px;
    display: flex; align-items: center; justify-content: center; gap: 40px;
  }
  .card {
    position: relative;
    width: 520px; height: 297px;
    background: linear-gradient(150deg, var(--card-edge), var(--card) 60%);
    border-radius: 4px;
    box-shadow: 0 12px 30px rgba(0,0,0,0.45);
  }
  .wordmark {
    font-family: "Montserrat", sans-serif;
    font-weight: 600;
    color: var(--gold);
    letter-spacing: 0.12em;
    text-transform: uppercase;
    display: flex; align-items: center; gap: 10px;
  }
  .wordmark-dot {
    width: 10px; height: 10px; border-radius: 50%;
    background: var(--gold); flex: none;
  }
  /* Front */
  .card-front .wordmark {
    position: absolute; left: 0; right: 0; top: 118px;
    justify-content: center; font-size: 20px;
  }
  .card-front .site {
    position: absolute; left: 0; right: 0; top: 172px;
    text-align: center;
    font-family: "Open Sans", sans-serif; font-size: 13px;
    color: var(--gold); letter-spacing: 0.02em;
  }
  /* Back */
  .card-back .wordmark {
    position: absolute; left: 24px; top: 132px; width: 170px;
    font-size: 13px; line-height: 1.35; align-items: flex-start;
  }
  .card-back .wordmark-dot { margin-top: 4px; }
  .divider {
    position: absolute; left: 206px; top: 62px;
    width: 2px; height: 176px; background: var(--gold);
  }
  .person {
    position: absolute; left: 228px; top: 60px;
  }
  .person-name {
    font-family: "Montserrat", sans-serif; font-weight: 700;
    font-size: 25px; color: var(--white); line-height: 1.1;
  }
  .person-role {
    font-family: "Montserrat", sans-serif; font-weight: 600;
    font-size: 13px; color: var(--gold); margin-top: 2px;
  }
  .contacts {
    position: absolute; left: 228px; top: 132px;
    list-style: none;
    font-family: "Open Sans", sans-serif; font-size: 13.5px;
    color: var(--white);
  }
  .contacts li {
    display: flex; align-items: center; gap: 10px; height: 24px;
    white-space: nowrap;
  }
  .contacts svg { width: 15px; height: 15px; flex: none; }
  .social-square {
    width: 13px; height: 13px; background: var(--gold);
    border-radius: 2px; flex: none; margin: 0 1px;
  }
  .cert-badge {
    position: absolute; right: 26px; top: 70px;
    width: 64px; height: 64px; border-radius: 50%;
    background: var(--white);
    border: 4px solid var(--card);
    box-shadow: 0 0 0 2px var(--white);
  }
</style>
</head>
<body>
<main class="stage">
  <section class="card card-front" aria-label="Business card front">
    <div class="wordmark"><span class="wordmark-dot"></span>Kestrel Building Works</div>
    <p class="site">www.kestrelbuildingworks.co.nz</p>
  </section>

  <section class="card card-back" aria-label="Business card back">
    <div class="wordmark"><span class="wordmark-dot"></span><span>Kestrel Building Works</span></div>
    <div class="divider"></div>
    <div class="person">
      <p class="person-name">Warren Pike</p>
      <p class="person-role">Director</p>
    </div>
    <ul class="contacts">
      <li>
        <svg viewBox="0 0 16 16" aria-hidden="true"><path fill="#c9965f" d="M3 2h3l1.5 3.5-2 1.2a8 8 0 0 0 3.8 3.8l1.2-2L14 10v3a1 1 0 0 1-1 1A11 11 0 0 1 2 3a1 1 0 0 1 1-1z"/></svg>
        0219462513
      </li>
      <li>
        <svg viewBox="0 0 16 16" aria-hidden="true"><rect x="1.5" y="3.5" width="13" height="9" fill="none" stroke="#c9965f" stroke-width="1.4"/><path d="M1.5 3.5 8 9l6.5-5.5" fill="none" stroke="#c9965f" stroke-width="1.4"/></svg>
        kestrelbuild.nz@mailbox-example.nz
      </li>
      <li>
        <svg viewBox="0 0 16 16" aria-hidden="true"><g fill="none" stroke="#c9965f" stroke-width="1.2"><circle cx="8" cy="8" r="6.3"/><ellipse cx="8" cy="8" rx="2.8" ry="6.3"/><path d="M1.7 8h12.6M2.8 4.7h10.4M2.8 11.3h10.4"/></g></svg>
        www.kestrelbuildingworks.co.nz
      </li>
      <li>
        <span class="social-square"></span>
        /kestrelbuild.nz
      </li>
    </ul>
    <div class="cert-badge" role="img" aria-label="Certified Trade Craftsmen membership badge"></div>
  </section>
</main>
</body>
</html>
```